Brennick Holdings Business Cards

These are professional business cards that are for my family office.
Put fake emails and phone numbers as of now until I finalize those components. This family office controls my families investments, assets, and future. The cards should be professional.
..
.
.
.
I just uploaded another variation of a logo I would like to see as a business card to I am inbeteen which logo to use

Target Market(s)

business

Industry/Entity Type

business

Contact Information for Business Card

Professional, wealth related, finance related.

Requirements
Must have
• Logo

```html
<!DOCTYPE html>
<html lang="en">
<head>
<meta charset="utf-8">
<title>Brennick Holdings – Business Cards</title>
<link rel="stylesheet" href="https://fonts.googleapis.com/css2?family=Marcellus+SC&family=Lato:wght@400&display=swap">
<style>
  :root {
    --backdrop: #26272b;
    --card: #171c2b;
    --card-edge: #1f2537;
    --ink: #e9eaee;
    --ink-soft: #c9ccd4;
    --rule: rgba(233, 234, 238, 0.35);
  }
  * { box-sizing: border-box; margin: 0; padding: 0; }
  html, body {
    width: 1200px;
    height: 952px;
    overflow: hidden;
    background: var(--backdrop);
  }
  .sheet {
    width: 1200px;
    height: 952px;
    display: flex;
    align-items: center;
    justify-content: center;
    gap: 44px;
  }
  .card {
    width: 520px;
    height: 297px;
    background: var(--card);
    border: 1px solid var(--card-edge);
    box-shadow: 0 18px 40px rgba(0, 0, 0, 0.45);
    position: relative;
    color: var(--ink);
  }

  /* Front: company name + contact */
  .card--front { display: flex; align-items: center; }
  .brand-block {
    width: 230px;
    display: flex;
    justify-content: center;
  }
  .brand-name {
    font-family: "Marcellus SC", serif;
    font-size: 19px;
    letter-spacing: 0.5px;
    color: var(--ink);
    white-space: nowrap;
  }
  .divider {
    width: 1px;
    height: 190px;
    background: linear-gradient(to bottom, transparent, var(--rule) 30%, var(--rule) 70%, transparent);
  }
  .contact-block { padding-left: 30px; }
  .person-name {
    font-family: "Marcellus SC", serif;
    font-size: 22px;
    letter-spacing: 0.6px;
    white-space: nowrap;
  }
  .person-title {
    font-family: "Lato", sans-serif;
    font-size: 14px;
    color: var(--ink-soft);
    margin-top: 2px;
  }
  .contact-list {
    list-style: none;
    margin-top: 18px;
    font-family: "Lato", sans-serif;
    font-size: 13px;
    color: var(--ink-soft);
  }
  .contact-list li {
    display: flex;
    align-items: center;
    gap: 8px;
    line-height: 22px;
    white-space: nowrap;
  }
  .contact-icon { width: 11px; height: 11px; fill: var(--ink-soft); flex: none; }

  /* Back: company name only */
  .card--back { display: flex; align-items: center; justify-content: center; }
  .back-name {
    font-family: "Marcellus SC", serif;
    font-size: 36px;
    letter-spacing: 1px;
    color: var(--ink);
    white-space: nowrap;
  }
</style>
</head>
<body>
<main class="sheet">
  <section class="card card--front">
    <div class="brand-block">
      <div class="brand-name">Brennick Holdings</div>
    </div>
    <div class="divider" aria-hidden="true"></div>
    <div class="contact-block">
      <div class="person-name">Daniel R. Hartwell</div>
      <div class="person-title">Managing Director</div>
      <ul class="contact-list">
        <li>
          <svg class="contact-icon" viewBox="0 0 16 16" aria-hidden="true"><path d="M3.6 1.2l2.2 2.6-1.3 1.8c.9 2 2.4 3.6 4.3 4.6l1.8-1.3 2.6 2.2-1.3 2.6C6.5 13.4 2.6 9.5 1 4z"/></svg>
          +00 123 456 78
        </li>
        <li>
          <svg class="contact-icon" viewBox="0 0 16 16" aria-hidden="true"><path d="M1 3h14v10H1z M1.6 3.6L8 9l6.4-5.4" stroke="#171c2b" stroke-width="1.2"/></svg>
          office@brennickmail.com
        </li>
        <li>
          <svg class="contact-icon" viewBox="0 0 16 16" aria-hidden="true"><circle cx="8" cy="8" r="7"/><path d="M1 8h14M8 1c-3 3.5-3 10.5 0 14M8 1c3 3.5 3 10.5 0 14" stroke="#171c2b" stroke-width="1" fill="none"/></svg>
          www.brennickholdings.com
        </li>
      </ul>
    </div>
  </section>

  <section class="card card--back">
    <div class="back-name">Brennick Holdings</div>
  </section>
</main>
</body>
</html>
```